Post Lockdown Ortho Special

We are running a special for (Ortho) Braces/Clear Aligner (Quorventa), till July 31st 2020. Up to $2,000 off with free Consultation and Xrays.

We need a ad to run in different formats.

Maybe something with: what better time to get braces when you have to wear a mask all the time.

Trying to rebuild our business and get people in for free consultations.

```html
<!DOCTYPE html>
<html lang="en">
<head>
<meta charset="utf-8">
<title>Post Lockdown Ortho Special</title>
<link rel="stylesheet" href="https://fonts.googleapis.com/css2?family=Montserrat:wght@300;400;500;700;800&display=swap">
<style>
  :root {
    --purple: #65449a;
    --white: #ffffff;
    --page: #ececee;
    --photo-light: #e9e6e8;
    --photo-warm: #d8c3b6;
    --photo-pink: #e7a9b9;
    --muted: #8a7f92;
  }
  * { box-sizing: border-box; margin: 0; padding: 0; }
  html, body {
    width: 1098px; height: 1200px; overflow: hidden;
    background: var(--page);
    font-family: "Montserrat", Arial, sans-serif;
  }
  .ad {
    position: absolute; left: 160px; top: 0;
    width: 778px; height: 1200px;
    background: var(--white);
  }
  .band { position: absolute; left: 0; width: 100%; background: var(--purple); color: var(--white); text-align: center; }
  .band--headline { top: 0; height: 249px; }
  .headline {
    position: absolute; top: 68px; left: 0; width: 100%;
    font-weight: 800; font-size: 23px; line-height: 31px;
    letter-spacing: 2.6px; text-transform: uppercase;
  }
  .photos { position: absolute; top: 254px; left: 0; width: 100%; height: 230px; }
  .photo { position: absolute; top: 0; height: 230px; }
  .photo--mask { left: 0; width: 372px; background: linear-gradient(90deg, var(--photo-light), var(--photo-warm) 50%, var(--photo-light)); }
  .photo--smile { left: 388px; width: 390px; background: linear-gradient(90deg, var(--photo-light), var(--photo-warm) 45%, var(--photo-pink)); }
  .band--offer { top: 490px; height: 438px; }
  .kicker { position: absolute; top: 50px; width: 100%; font-weight: 300; font-size: 29px; letter-spacing: 5px; }
  .kicker-strong { position: absolute; top: 86px; width: 100%; font-weight: 800; font-size: 23px; letter-spacing: 2.6px; }
  .rule { position: absolute; top: 150px; left: 339px; width: 106px; height: 3px; background: var(--white); }
  .offer-amount { position: absolute; top: 186px; width: 100%; font-weight: 700; font-size: 47px; }
  .offer-detail { position: absolute; top: 253px; width: 100%; font-weight: 500; font-size: 26px; line-height: 34px; }
  .offer-deadline {
    position: absolute; top: 338px; left: 214px; width: 352px; height: 39px;
    border: 1.5px solid var(--white); border-radius: 20px;
    font-weight: 500; font-size: 21px; line-height: 36px;
  }
  .brand { position: absolute; top: 962px; left: 208px; display: flex; align-items: center; gap: 18px; }
  .brand-dot { width: 96px; height: 96px; border-radius: 50%; background: var(--purple); }
  .brand-name { color: var(--purple); font-weight: 700; font-size: 24px; line-height: 28px; text-transform: uppercase; letter-spacing: 1px; }
  .brand-doctor { margin-top: 8px; color: var(--muted); font-weight: 400; font-size: 12px; letter-spacing: 2px; text-transform: uppercase; border-top: 1px solid var(--muted); padding-top: 4px; }
  .call { position: absolute; top: 1126px; left: 0; width: 100%; text-align: center; color: var(--purple); font-size: 33px; display: flex; justify-content: center; align-items: center; gap: 10px; }
  .call-label { font-weight: 400; }
  .call-number { font-weight: 700; font-size: 37px; }
  .call svg { width: 32px; height: 32px; }
  .footer-strip { position: absolute; bottom: 0; left: 0; width: 100%; height: 10px; background: var(--purple); }
</style>
</head>
<body>
  <main class="ad">
    <section class="band band--headline">
      <h1 class="headline">What better time to<br>get braces<br>when you have to wear<br>a mask all the time</h1>
    </section>

    <section class="photos">
      <div class="photo photo--mask" role="img" aria-label="Young woman wearing a surgical face mask"></div>
      <div class="photo photo--smile" role="img" aria-label="Close-up smile with pink lips showing teeth with braces"></div>
    </section>

    <section class="band band--offer">
      <p class="kicker">POST LOCKDOWN</p>
      <p class="kicker-strong">ORTHO SPECIAL</p>
      <div class="rule"></div>
      <p class="offer-amount">UP TO $2,000 OFF</p>
      <p class="offer-detail">ON BRACES/CLEAR ALIGNER (QUORVENTA)<br>WITH FREE CONSULTATION AND XRAYS</p>
      <p class="offer-deadline">OFFER TILL JULY 31ST 2020</p>
    </section>

    <div class="brand">
      <div class="brand-dot"></div>
      <div>
        <p class="brand-name">Pinecrest<br>Family Dentistry</p>
        <p class="brand-doctor">Dr Helena Marsh</p>
      </div>
    </div>

    <p class="call">
      <span class="call-label">CALL TODAY</span>
      <svg viewBox="0 0 24 24" aria-hidden="true"><path d="M6.6 10.8a15.1 15.1 0 0 0 6.6 6.6l2.2-2.2a1 1 0 0 1 1-.25 11.4 11.4 0 0 0 3.6.57 1 1 0 0 1 1 1V20a1 1 0 0 1-1 1A17 17 0 0 1 3 4a1 1 0 0 1 1-1h3.5a1 1 0 0 1 1 1c0 1.25.2 2.45.57 3.57a1 1 0 0 1-.25 1z" fill="none" stroke="currentColor" stroke-width="1.8"/><path d="M14 3a7 7 0 0 1 7 7M14 6.5a3.5 3.5 0 0 1 3.5 3.5" fill="none" stroke="currentColor" stroke-width="1.8" stroke-linecap="round"/></svg>
      <span class="call-number">928 555 0147</span>
    </p>

    <div class="footer-strip"></div>
  </main>
</body>
</html>
```